Re-design a highly converting profile page for my website

My website allows people to book a mentor for long-term mentorship as well as sessions. I would like to re-design this site within our branding guidelines to give people the best profile possible.

Please give this website a modern look and concentrate on the CTA and conversion rates. This is a highly converting site and it should stay that way or even get better!

Please also keep menu bar & footer in tact

Target Market(s)

Developers, Designers, Entrepreneurs in the Tech industry

Number of Pages Required

1 page

Requirements
Must have
• Strong CTA, existing color palette, testimonials and major elements
Nice to have
• Modern look, easy to see CTA, easy to scan offer. Not too crowded
Should not have
• No reporpusing. It is and stays a profile page

```html
<!DOCTYPE html>
<html lang="en">
<head>
<meta charset="utf-8">
<title>Jordan Hale – Mentor Profile</title>
<link href="https://fonts.googleapis.com/css2?family=Poppins:wght@400;500;600;700&display=swap" rel="stylesheet">
<style>
:root{
  --navy:#1d2a4a;
  --teal:#1bb8ad;
  --teal-light:#dff5f3;
  --blue:#2f7fd8;
  --bg:#f3f5f8;
  --card:#ffffff;
  --text:#28324a;
  --muted:#7b8497;
  --line:#e2e6ed;
  --star:#f5a623;
}
*{box-sizing:border-box;margin:0;padding:0}
html,body{width:1200px;height:2528px;overflow:hidden}
body{background:var(--bg);font-family:"Poppins",sans-serif;color:var(--text);position:relative;font-size:13px;line-height:1.55}
.abs{position:absolute}
.deco{position:absolute;left:0;top:0;pointer-events:none}
.btn{display:inline-flex;align-items:center;justify-content:center;border-radius:4px;font-weight:600;font-size:12px;height:34px;padding:0 18px;text-decoration:none;white-space:nowrap}
.btn-teal{background:var(--teal);color:#fff}
.btn-navy{background:var(--navy);color:#fff}
.btn-white{background:#fff;color:var(--navy)}
.btn-outline{border:1.5px solid var(--teal);color:var(--teal);background:#fff}

.site-header{left:0;top:0;width:1200px;height:64px;display:flex;align-items:center;justify-content:space-between;padding:0 60px}
.brand{display:flex;align-items:center;gap:8px;font-weight:700;color:var(--navy);font-size:15px}
.brand-dot{width:14px;height:14px;border-radius:50%;background:var(--teal)}
.nav{display:flex;align-items:center;gap:26px;font-size:12px;font-weight:500;color:var(--navy)}
.nav .btn{height:30px;padding:0 16px}

.profile-card{left:120px;top:64px;width:960px;height:310px;background:var(--card);border-radius:8px;box-shadow:0 6px 24px rgba(29,42,74,.07)}
.avatar{left:60px;top:18px;width:260px;height:260px;border-radius:50%;background:radial-gradient(circle at 50% 40%,#e9c2a8 0,#d79d84 35%,#c0566a 70%,#9fb8c8 100%);border:8px solid #fff;box-shadow:0 4px 18px rgba(0,0,0,.12)}
.profile-name{left:540px;top:52px;font-size:28px;font-weight:700;color:var(--navy)}
.profile-role{left:540px;top:92px;font-size:14px;color:var(--muted)}
.badge-top{right:30px;top:30px;background:var(--teal);color:#fff;font-size:11px;font-weight:600;padding:4px 12px;border-radius:3px}
.profile-meta{left:540px;top:130px;right:30px;display:flex;justify-content:space-between;font-size:12px;color:var(--muted);padding:10px 0;border-top:1px solid var(--line);border-bottom:1px solid var(--line)}
.stars{color:var(--star);letter-spacing:2px;margin-right:6px}
.profile-tags{left:540px;top:196px;right:30px;display:flex;justify-content:space-between;font-size:11px;color:var(--navy)}
.profile-tags span{display:flex;align-items:center;gap:6px;white-space:nowrap}
.profile-tags i{width:10px;height:10px;border-radius:50%;border:2px solid var(--teal);display:inline-block}
.bio{left:120px;top:392px;width:960px;font-size:12px;color:var(--muted)}
.bio p{margin-bottom:10px}
.bio a{color:var(--teal);text-decoration:none}

.trial{left:120px;top:560px;width:960px;height:100px;background:var(--navy);border-radius:6px;display:flex;align-items:center;padding:0 40px;color:#fff}
.trial h2{font-size:26px;font-weight:700;color:var(--teal);margin-right:auto}
.price{background:var(--teal);padding:8px 18px;border-radius:4px;margin-right:40px;text-align:center;line-height:1.1}
.price strong{font-size:34px;display:block}
.price small{font-size:11px}
.trial-actions{display:flex;flex-direction:column;align-items:center;gap:6px}
.trial-actions .row{display:flex;gap:12px}
.trial-actions small{font-size:10px;color:#b9c3d8}

.section-title{font-size:22px;font-weight:700;color:var(--navy)}
.expect{left:120px;top:700px;width:960px}
.expect-list{list-style:none;margin-top:18px;width:440px}
.expect-list li{display:flex;gap:10px;align-items:flex-start;font-size:12px;margin-bottom:12px}
.tick{flex:none;width:16px;height:16px;border-radius:3px;background:var(--teal);display:flex;align-items:center;justify-content:center}
.session-box{left:520px;top:40px;width:400px;height:190px;background:#fff;border:1px solid var(--line);border-radius:6px;text-align:center;padding:50px 40px 0}
.session-box h3{font-size:15px;font-weight:600;color:var(--navy);line-height:1.4;margin-bottom:16px}
.burst{position:absolute}
.burst span{position:absolute;inset:0;display:flex;align-items:center;justify-content:center;color:#fff;font-weight:700;text-align:center;line-height:1.1}

.stats{left:300px;top:996px;width:600px;display:flex;gap:40px}
.stat{flex:1;background:#fff;border-radius:6px;padding:12px 16px;display:flex;gap:12px;align-items:center;font-size:11px;color:var(--muted)}
.stat b{display:block;color:var(--navy);font-size:12px}
.stat-icon{width:28px;height:28px;border-radius:50%;background:var(--teal-light);flex:none;display:flex;align-items:center;justify-content:center}

.skills{left:120px;top:1070px;width:960px;text-align:center}
.skill-list{margin-top:18px;display:flex;flex-wrap:wrap;gap:10px;justify-content:center}
.skill-list span{background:#fff;border:1px solid var(--line);border-radius:3px;font-size:10px;padding:5px 11px;color:var(--text)}

.testimonials{left:120px;top:1310px;width:960px;text-align:center}
.t-grid{display:flex;gap:24px;margin-top:22px;text-align:left}
.t-card{flex:1;background:#fff;border-radius:6px;padding:24px 22px;font-size:11px;color:var(--muted);height:230px;position:relative}
.t-card .quote{color:var(--teal);font-size:30px;font-weight:700;line-height:.6;display:block;margin-bottom:8px}
.t-card b{position:absolute;left:22px;bottom:20px;color:var(--navy);font-size:12px}
.t-actions{margin-top:22px;display:flex;gap:14px;justify-content:center}

.course{left:120px;top:1700px;width:960px;height:120px;background:var(--teal);border-radius:6px;padding:22px 40px;color:#fff}
.course h2{font-size:24px;font-weight:700;line-height:1.2;color:var(--navy)}
.course h2 span{color:#fff}
.course-link{display:flex;margin-top:10px;gap:8px}
.course-link .url{background:#fff;color:var(--muted);font-size:11px;padding:0 12px;height:30px;display:flex;align-items:center;border-radius:3px;width:230px}
.course-link .btn{height:30px;font-size:11px}

.links{left:120px;top:1875px;width:960px;display:grid;grid-template-columns:repeat(3,1fr);gap:22px 40px;font-size:11px}
.links b{display:block;color:var(--navy);font-weight:600}
.links a{color:var(--teal);text-decoration:none}

.similar{left:120px;top:2080px;width:960px;display:flex;gap:40px}
.mentor-card{flex:1;background:#fff;border-radius:6px;padding:20px;display:flex;gap:16px;height:150px}
.mini-avatar{width:56px;height:56px;border-radius:50%;flex:none;background:linear-gradient(135deg,#c9a48c,#6c7a92)}
.mentor-card b{display:block;color:var(--navy);font-size:14px}
.mentor-card p{font-size:11px;color:var(--muted)}
.mentor-card .tags{display:flex;gap:6px;margin-top:10px;flex-wrap:wrap}
.mentor-card .tags span{border:1px solid var(--line);font-size:9px;padding:3px 8px;border-radius:3px}

.site-footer{left:0;top:2280px;width:1200px;height:248px;background:#fff;padding:40px 120px;display:flex;gap:60px;font-size:10px;color:var(--muted)}
.footer-about{width:380px}
.footer-about .brand{margin-bottom:10px}
.socials{display:flex;gap:10px;margin-top:14px}
.socials i{width:14px;height:14px;border-radius:50%;background:var(--navy);display:block}
.footer-col{flex:1}
.footer-col b{display:block;color:var(--navy);font-size:11px;margin-bottom:8px}
.footer-col a{display:block;color:var(--muted);text-decoration:none;margin-bottom:4px}
</style>
</head>
<body>

<svg class="deco" width="1200" height="2528" viewBox="0 0 1200 2528" aria-hidden="true">
  <path d="M0 110 C120 50 250 70 300 150 C350 240 280 320 160 340 C90 350 30 340 0 330Z" fill="#1d2a4a"/>
  <path d="M900 250 C1040 200 1200 260 1200 260 L1200 520 C1100 560 950 480 900 250Z" fill="#e8ecf2"/>
  <path d="M0 1260 C200 1220 420 1300 600 1280 C800 1258 1000 1200 1200 1240 L1200 1680 L0 1680Z" fill="#eaedf2"/>
  <path d="M980 1900 C1080 1860 1160 1900 1200 1930 L1200 2060 C1120 2040 1020 2010 980 1900Z" fill="#e2e7ee"/>
</svg>

<header class="site-header abs">
  <div class="brand"><span class="brand-dot"></span>MentorTrack</div>
  <nav class="nav">
    <span>Find a Mentor</span>
    <span>For Businesses</span>
    <span>Book a Demo</span>
    <a class="btn btn-teal">Login</a>
    <a class="btn btn-navy">Get Started</a>
  </nav>
</header>

<section class="profile-card abs">
  <div class="avatar abs" role="img" aria-label="Portrait photo of the mentor"></div>
  <div class="badge-top abs">Top Mentor</div>
  <h1 class="profile-name abs">Jordan Hale</h1>
  <div class="profile-role abs">Director of Product · Ridgeway Insurance</div>
  <div class="profile-meta abs">
    <span>● United States of America</span>
    <span><span class="stars">★★★★★</span>4.9 (18 Reviews)</span>
  </div>
  <div class="profile-tags abs">
    <span><i></i>Personal Chat</span>
    <span><i></i>Hands-On Work</span>
    <span><i></i>Challenges &amp; Projects</span>
    <span><i></i>Live Calls</span>
  </div>
</section>

<div class="bio abs">
  <p>Jordan is a passionate product leader with over a decade of experience shipping digital products in fast-moving teams. From early startups to large insurers, Jordan has guided new product managers through their first roadmaps, hard launches and tough stakeholder conversations, and loves helping people grow their craft.</p>
  <p>Jordan currently leads product strategy at Ridgeway Insurance and writes about modern product practice. Read more on the <a>blog</a> or join the <a>newsletter</a> to get weekly tips on discovery, delivery and career growth.</p>
</div>

<section class="trial abs">
  <h2>7 Day Free Trial!</h2>
  <div class="price"><strong>$240</strong><small>per month</small></div>
  <div class="trial-actions">
    <div class="row"><a class="btn btn-teal">Apply for Mentorship</a><a class="btn btn-white">Book a Session</a></div>
    <small>Cancel anytime · 7-day refund</small>
  </div>
</section>

<section class="expect abs">
  <h2 class="section-title">What can I expect?</h2>
  <ul class="expect-list">
    <li><span class="tick"><svg width="10" height="10" viewBox="0 0 10 10"><path d="M1.5 5.2l2.2 2.2L8.5 2.6" stroke="#fff" stroke-width="1.8" fill="none"/></svg></span>Unlimited access to the mentor via chat or email and a shared space</li>
    <li><span class="tick"><svg width="10" height="10" viewBox="0 0 10 10"><path d="M1.5 5.2l2.2 2.2L8.5 2.6" stroke="#fff" stroke-width="1.8" fill="none"/></svg></span>You will have a 1 hour call to kick off the mentorship</li>
    <li><span class="tick"><svg width="10" height="10" viewBox="0 0 10 10"><path d="M1.5 5.2l2.2 2.2L8.5 2.6" stroke="#fff" stroke-width="1.8" fill="none"/></svg></span>Work on your own tasks and have them reviewed in detail</li>
    <li><span class="tick"><svg width="10" height="10" viewBox="0 0 10 10"><path d="M1.5 5.2l2.2 2.2L8.5 2.6" stroke="#fff" stroke-width="1.8" fill="none"/></svg></span>Includes regular 1-on-1 calls, per agreement with your mentor</li>
    <li><span class="tick"><svg width="10" height="10" viewBox="0 0 10 10"><path d="M1.5 5.2l2.2 2.2L8.5 2.6" stroke="#fff" stroke-width="1.8" fill="none"/></svg></span>Flat fee of $240 per month, no hidden costs</li>
  </ul>
  <div class="session-box abs">
    <div class="burst" style="left:-36px;top:-40px;width:84px;height:84px">
      <svg width="84" height="84" viewBox="0 0 84 84"><polygon fill="#2f7fd8" points="42,0 50,14 65,7 66,23 82,26 73,40 84,52 68,57 70,74 54,70 46,84 38,70 22,76 22,59 6,55 14,42 2,29 18,25 18,9 34,14"/></svg>
      <span style="font-size:15px">NEW</span>
    </div>
    <h3>"How to Become a Product Manager Coaching Session for Mentees" Session</h3>
    <a class="btn btn-navy">Book Now</a>
  </div>
</section>

<section class="stats abs">
  <div class="stat"><span class="stat-icon"><svg width="14" height="14" viewBox="0 0 14 14"><circle cx="7" cy="7" r="5.5" stroke="#1bb8ad" stroke-width="1.6" fill="none"/><path d="M7 4v3.2l2 1.4" stroke="#1bb8ad" stroke-width="1.6" fill="none"/></svg></span><div><b>Average response time</b>Usually responds within a few hours</div></div>
  <div class="stat"><span class="stat-icon"><svg width="14" height="14" viewBox="0 0 14 14"><circle cx="5" cy="5" r="2.4" fill="#1bb8ad"/><circle cx="10" cy="6" r="2" fill="#1bb8ad"/><path d="M1 12c0-3 8-3 8 0M8 12c0-2 5-2 5 0" stroke="#1bb8ad" stroke-width="1.4" fill="none"/></svg></span><div><b>Part of these groups</b>Product Leaders · Career Switchers</div></div>
</section>

<section class="skills abs">
  <h2 class="section-title">Skills taught by mentor</h2>
  <div class="skill-list">
    <span>Product Marketing</span><span>Product</span><span>Product Management</span><span>Strategy</span><span>Roadmapping</span><span>Discovery</span><span>UX</span><span>Product Leadership</span>
    <span>Career Growth</span><span>Stakeholders</span><span>User Research</span><span>Prioritization</span><span>Analytics</span><span>Agile Product</span><span>Interviewing</span><span>Growth</span>
    <span>Lean Product Methods</span><span>OKRs</span><span>B2B</span><span>SaaS</span><span>Launch</span>
  </div>
</section>

<section class="testimonials abs">
  <h2 class="section-title">Testimonials</h2>
  <div class="t-grid">
    <div class="t-card"><span class="quote">“</span>Jordan helped me focus on what mattered in my first product role. Every call was practical, honest and full of clear next steps. I left each session knowing exactly what to try next, and my confidence with my team grew week after week.<b>Alicia</b></div>
    <div class="t-card"><span class="quote">“</span>I was unsure how to switch into product from engineering. Jordan walked me through case studies, reviewed my portfolio and prepared me for interviews. Within two months I landed a new role. I would recommend this mentorship to anyone.<b>Ben</b></div>
    <div class="t-card"><span class="quote">“</span>This is a fantastic mentor to have in your corner. Jordan shares real stories from years of leading teams, explains difficult trade-offs simply and always makes time for questions. Great value and a very kind, thoughtful guide.<b>Carla</b></div>
  </div>
  <div class="t-actions"><a class="btn btn-teal">View all Reviews</a><a class="btn btn-outline">Write a Review</a></div>
</section>

<section class="course abs">
  <h2>Aspiring or new PM? <span>Or looking to level up?</span><br>Check out my new Product Management course here:</h2>
  <div class="course-link"><span class="url">www.pmcourse-example.com</span><a class="btn btn-navy">ENROLL IN THE COURSE</a></div>
  <div class="burst" style="right:40px;top:16px;width:92px;height:92px">
    <svg width="92" height="92" viewBox="0 0 84 84"><polygon fill="#2f7fd8" points="42,0 50,14 65,7 66,23 82,26 73,40 84,52 68,57 70,74 54,70 46,84 38,70 22,76 22,59 6,55 14,42 2,29 18,25 18,9 34,14"/></svg>
    <span style="font-size:17px">25%<br>off</span>
  </div>
</section>

<section class="links abs">
  <div><b>Author, Shipping With Purpose</b><a>www.shipping-purpose-book.com</a></div>
  <div><b>Blog</b><a>www.jordanhale-blog.com</a></div>
  <div><b>The Product Path Newsletter</b><a>www.productpath-letter.com</a></div>
  <div><b>Author, Know Your Craft</b><a>www.know-your-craft.com</a></div>
  <div><b>Top Writer in Startup Category</b><a>www.startup-writers.com</a></div>
  <div><b>The Product Path Podcast</b><a>www.productpath-podcast.com</a></div>
  <div><b>Speaker</b><a>www.jordanhale-talks.com</a></div>
</section>

<section class="similar abs">
  <div class="mentor-card">
    <div class="mini-avatar" role="img" aria-label="Portrait photo of a similar mentor"></div>
    <div><b>Theo Garland</b><p>Senior Product Manager</p><p>He helped me a lot with my career switch.</p>
      <div class="tags"><span>Product Management</span><span>UX</span><span>Agile</span></div></div>
  </div>
  <div class="mentor-card">
    <div class="mini-avatar" role="img" aria-label="Portrait photo of a similar mentor"></div>
    <div><b>Marcus Reed</b><p>Head of Product</p><p>Marcus helped me build a good track for my team.</p>
      <div class="tags"><span>Product Strategy</span><span>Leadership</span></div></div>
  </div>
</section>

<footer class="site-footer abs">
  <div class="footer-about">
    <div class="brand"><span class="brand-dot"></span>MentorTrack</div>
    <p>Your trusted source to find highly-vetted mentors &amp; industry professionals to move your career ahead.</p>
    <p>© 2024 MentorTrack. All rights reserved.</p>
    <div class="socials"><i></i><i></i><i></i></div>
  </div>
  <div class="footer-col"><b>Platform</b><a>Browse Mentors</a><a>Book a Session</a><a>Become a Mentor</a><a>Mentorship for Teams</a><a>FAQ</a></div>
  <div class="footer-col"><b>Resources</b><a>Blog</a><a>Newsletter</a><a>Success Stories</a><a>Community</a></div>
  <div class="footer-col"><b>Company</b><a>About Us</a><a>Terms of Service</a><a>Privacy Policy</a><a>Contact</a></div>
</footer>

</body>
</html>
```